Clean, creative business Wordpress Site

Our company is building a website via Wordpress and needs a clean, no fuss, modern looking design that reflects our company brand (see attached logos).

In addition, the company is a woman owned business (no middle-aged white guy stock photos please) and primarily works with the oil & gas industry. We would prefer no images with direct references to energy (rigs, windmills, solar panels, etc.). Part of our consulting is providing thought leadership around energy politics and policy so creative ways to incorporate that visually will be appreciated as well.

Site map of pages below:

Home
- About
- Team
- Expertise
- Blog

We prefer a header image that includes the company logo and easy to identify and navigate menus.

Target Market(s)

Energy professionals, Executives

Industry/Entity Type

Consulting

Font styles to use
Serif

Colors
85acd3
0255a3
cedeed
ffffff

Requirements
Must have
• Clean and easy to navigate, clear menus, simple design that reflects company logo.

```html
<!DOCTYPE html>
<html lang="en">
<head>
<meta charset="utf-8">
<title>Corvalis Energy</title>
<link href="https://fonts.googleapis.com/css2?family=Montserrat:wght@400;600;700&family=Open+Sans:wght@400;600;700&family=Playfair+Display:ital@1&family=Libre+Baskerville&display=swap" rel="stylesheet">
<style>
:root{
  --navy:#0e4f86;
  --blue:#0255a3;
  --sky:#85acd3;
  --pale:#cedeed;
  --bright:#3fa2e8;
  --ink:#1b3b5c;
  --text:#5a6570;
  --muted:#9aa3ad;
  --black:#0d0f12;
  --foot:#0f1a26;
  --white:#ffffff;
}
*{box-sizing:border-box;margin:0;padding:0}
html,body{width:1200px;height:4615px;overflow:hidden}
body{position:relative;background:var(--white);font-family:"Open Sans",Arial,sans-serif;color:var(--text)}
section,header,footer{position:absolute;left:0;width:1200px}
h2.section-title{position:absolute;left:0;width:1200px;text-align:center;font-family:"Montserrat",sans-serif;font-weight:700;font-size:50px;color:var(--navy)}
.section-sub{position:absolute;left:0;width:1200px;text-align:center;font-family:"Montserrat",sans-serif;font-size:15px;letter-spacing:3px;color:var(--muted);text-transform:uppercase}
.notch{position:absolute;left:560px;width:80px;height:30px}

/* hero */
.hero{top:0;height:738px;background:linear-gradient(180deg,#3a3226 0%,#9a6a34 35%,#d99a4a 55%,#5a4a3a 75%,#2a2620 100%)}
.hero-photo{position:absolute;inset:0}
.brand{position:absolute;left:185px;top:22px;display:flex;align-items:center;gap:12px;color:var(--white);font-family:"Libre Baskerville",serif;font-size:30px;letter-spacing:1px}
.brand-mark{width:40px;height:40px;border-radius:50%;background:var(--blue)}
.nav{position:absolute;left:606px;top:42px;display:flex;gap:24px;font-family:"Montserrat",sans-serif;font-size:12px;color:var(--white);white-space:nowrap}
.nav .active{border-bottom:3px solid var(--sky);padding-bottom:8px}
.search{position:absolute;left:966px;top:30px;width:44px;height:40px;border:2px solid rgba(255,255,255,.7)}
.hero-box{position:absolute;left:215px;top:283px;width:770px;height:332px;background:rgba(10,10,15,.72);text-align:center;padding:40px 30px 0}
.hero-box h1{font-family:"Montserrat",sans-serif;font-size:56px;font-weight:700;color:var(--white);letter-spacing:1px}
.hero-box p{margin-top:14px;font-size:17px;line-height:28px;color:var(--white)}
.btn-outline{display:inline-block;margin-top:30px;padding:12px 30px;border:2px solid var(--white);color:var(--white);font-family:"Montserrat",sans-serif;font-size:13px;font-weight:600;letter-spacing:1px}
.hero-dots{position:absolute;left:1170px;top:570px}
.hero-dots span{display:block;width:8px;height:8px;border-radius:50%;background:var(--white);margin-bottom:12px;opacity:.6}
.hero-dots span:first-child{opacity:1}

/* about */
.about{top:738px;height:702px;background:linear-gradient(180deg,#ffffff 0%,#f0f0f0 60%,#e4e4e4 100%)}
.about .lead{position:absolute;left:230px;width:740px;top:200px;text-align:center;font-style:italic;font-size:17px;line-height:26px;color:var(--text)}
.feature{position:absolute;top:312px;width:262px;text-align:center}
.feature-tab{height:88px;background:var(--navy);border-radius:6px 6px 0 0}
.feature-icon{position:absolute;left:101px;top:34px;width:60px;height:60px;border-radius:50%;background:var(--white);border:4px solid var(--pale)}
.feature h3{margin-top:40px;font-family:"Montserrat",sans-serif;font-size:16px;font-weight:700;color:var(--ink)}
.feature h3 span{color:var(--sky)}
.feature p{margin:10px 12px 0;font-size:13px;line-height:19px}
.btn-small{display:inline-block;margin-top:16px;padding:7px 16px;background:var(--navy);color:var(--white);font-family:"Montserrat",sans-serif;font-size:11px;font-weight:700;border-radius:3px}

/* team */
.team{top:1440px;height:714px;background:#f1f1f1}
.card{position:absolute;background:var(--white);box-shadow:0 2px 8px rgba(0,0,0,.12)}
.team .card{top:215px;width:252px;height:407px}
.photo{height:228px;background:linear-gradient(160deg,#d6dbe0,#8fa0b2 60%,#3d5268)}
.card-body{padding:22px 20px 0;font-size:12px;line-height:17px}
.card-body h4{font-family:"Montserrat",sans-serif;font-size:14px;font-weight:600;color:#333}
.role{font-family:"Libre Baskerville",serif;font-style:italic;font-size:12px;color:var(--muted);margin:4px 0 12px}
.socials{display:flex;gap:10px;margin-top:16px}
.socials i{width:12px;height:12px;background:#555;border-radius:2px}
.dots{position:absolute;left:0;width:1200px;text-align:center}
.dots i{display:inline-block;width:10px;height:10px;border-radius:50%;border:1px solid #333;margin:0 2px}
.dots i:first-child{background:#333}

/* hiring */
.hiring{top:2154px;height:446px;background:linear-gradient(135deg,#0a3e73 0%,#1a5f99 45%,#0c4a86 100%);text-align:center;color:var(--white)}
.hiring h2{position:absolute;top:90px;width:1200px;font-family:"Montserrat",sans-serif;font-size:52px;font-weight:600;letter-spacing:2px}
.hiring p{position:absolute;left:160px;width:880px;top:200px;font-family:"Playfair Display",serif;font-style:italic;font-size:19px;line-height:33px}
.hiring .btn-outline{position:absolute;left:477px;top:325px;width:246px;margin:0;border-radius:30px;font-size:17px}

/* expertise */
.expertise{top:2600px;height:354px;background:var(--black);color:var(--white)}
.expertise h3{position:absolute;left:170px;top:70px;font-family:"Montserrat",sans-serif;font-size:20px;font-weight:700}
.expertise .tag{position:absolute;left:170px;top:103px;font-size:11px;font-weight:600;letter-spacing:.5px}
.skill{position:absolute;width:415px;font-size:13px}
.skill .track{margin-top:6px;height:6px;background:var(--white)}
.skill .fill{height:6px;background:var(--bright)}
.skill b{color:var(--bright);font-weight:600}

/* posts */
.posts{top:2954px;height:776px;background:#f1f1f1}
.posts .card{top:216px;width:252px;height:393px}
.posts .photo{height:208px;background:linear-gradient(160deg,#c8c2b8,#7e7a76 55%,#3c4450)}
.read{margin-top:16px;font-size:12px;color:#333}
.btn-pill{position:absolute;left:513px;top:692px;width:174px;height:50px;line-height:50px;text-align:center;background:var(--navy);color:var(--white);border-radius:25px;font-family:"Montserrat",sans-serif;font-size:13px;font-weight:600}

/* testimonial */
.testimonial{top:3730px;height:516px;background:linear-gradient(180deg,#1e4f7d 0%,#2f6a9a 50%,#173e63 100%);color:var(--white);text-align:center}
.testimonial h3{position:absolute;top:82px;width:1200px;font-family:"Montserrat",sans-serif;font-size:22px;font-weight:600;letter-spacing:3px}
.testimonial .section-sub{top:115px;color:var(--pale);font-size:13px}
.quote-box{position:absolute;left:231px;top:193px;width:738px;height:225px;background:#3b9df0;padding:120px 50px 0;font-size:13px;line-height:19px}
.avatar{position:absolute;left:548px;top:152px;width:104px;height:104px;border-radius:50%;background:linear-gradient(180deg,#e6e6e6,#9a9a9a);border:4px solid var(--white)}
.client{position:absolute;top:262px;width:1200px;font-family:"Montserrat",sans-serif;font-size:19px;line-height:22px;letter-spacing:2px}
.client small{display:block;font-size:12px;line-height:16px;letter-spacing:0}
.quote-mark{position:absolute;left:280px;top:245px;width:36px;height:30px}

/* footer */
.site-footer{top:4246px;height:369px;background:var(--foot);color:var(--white);font-size:12px}
.col{position:absolute;top:70px}
.col h5{font-family:"Montserrat",sans-serif;font-size:13px;font-weight:700;margin-bottom:22px}
.col p{line-height:17px;color:#cfd6dd}
.contact-line{display:flex;align-items:center;gap:10px;margin-top:10px;color:#cfd6dd}
.contact-line svg{width:12px;height:12px}
.links li{list-style:none;margin-bottom:9px;color:#cfd6dd;font-size:11px}
.field{width:196px;height:26px;background:var(--white);margin-bottom:10px;color:#888;font-size:10px;padding:6px 8px}
.subscribe{display:inline-block;padding:6px 12px;background:var(--bright);font-size:10px}
.foot-rule{position:absolute;left:231px;top:302px;width:738px;height:1px;background:#34404d}
.copy{position:absolute;left:231px;top:337px;font-size:10px;color:#9aa3ad}
.foot-brand{position:absolute;left:490px;top:318px;display:flex;align-items:center;gap:10px;font-family:"Libre Baskerville",serif;font-size:22px;color:var(--sky)}
.foot-brand .brand-mark{width:32px;height:32px}
.foot-social{position:absolute;left:835px;top:322px;display:flex;gap:8px}
.foot-social i{width:28px;height:28px;border-radius:50%;background:#3c77b8}
</style>
</head>
<body>

<header class="hero">
  <div class="hero-photo" role="img" aria-label="City skyline and bridge at sunset over water"></div>
  <div class="brand"><span class="brand-mark"></span>Corvalis Energy</div>
  <nav class="nav"><span class="active">HOME</span><span>ABOUT</span><span>TEAM</span><span>EXPERTISE</span><span>BLOG</span></nav>
  <div class="search"><svg viewBox="0 0 40 36" width="40" height="36"><circle cx="18" cy="16" r="7" fill="none" stroke="#fff" stroke-width="2"/><line x1="23" y1="21" x2="28" y2="26" stroke="#fff" stroke-width="2"/></svg></div>
  <div class="hero-box">
    <h1>CORVALIS ENERGY</h1>
    <p>Lorem Ipsum is simply dummy text of the printing and typesetting industry. Lorem Ipsum has been the industry's standard dummy text ever since the 1500s, when an unknown printer took a galley of type and scrambled it to make a type specimen book.</p>
    <span class="btn-outline">CLICK HERE TO READ MORE</span>
  </div>
  <div class="hero-dots"><span></span><span></span><span></span></div>
</header>

<section class="about">
  <svg class="notch" style="top:0" viewBox="0 0 80 30"><path d="M0 0 L40 26 L80 0Z" fill="#2a2620"/><path d="M30 8 L40 15 L50 8" fill="none" stroke="#fff" stroke-width="2"/></svg>
  <h2 class="section-title" style="top:100px">About Us</h2>
  <p class="lead">Lorem Ipsum is simply dummy text of the printing and typesetting industry. Lorem Ipsum has been the industry's standard dummy text ever since the 1500s, when an unknown printer took a galley of type and scrambled it to make a type specimen book.</p>
  <div class="feature" style="left:190px"><div class="feature-tab"></div><div class="feature-icon"></div><h3>HEADING <span>POINT 1</span></h3><p>Lorem Ipsum is simply dummy text of the printing and typesetting industry. Lorem Ipsum has been the industry's standard dummy text ever since the 1500s.</p><span class="btn-small">READ MORE ›</span></div>
  <div class="feature" style="left:468px"><div class="feature-tab"></div><div class="feature-icon"></div><h3>HEADING <span>POINT 1</span></h3><p>Lorem Ipsum is simply dummy text of the printing and typesetting industry. Lorem Ipsum has been the industry's standard dummy text ever since the 1500s.</p><span class="btn-small">READ MORE ›</span></div>
  <div class="feature" style="left:748px"><div class="feature-tab"></div><div class="feature-icon"></div><h3>HEADING <span>POINT 1</span></h3><p>Lorem Ipsum is simply dummy text of the printing and typesetting industry. Lorem Ipsum has been the industry's standard dummy text ever since the 1500s.</p><span class="btn-small">READ MORE ›</span></div>
</section>

<section class="team">
  <h2 class="section-title" style="top:60px">Our Team</h2>
  <div class="section-sub" style="top:128px">Our creative minds will make your ideas possible</div>
  <div class="card" style="left:170px"><div class="photo" role="img" aria-label="Team member portrait"></div><div class="card-body"><h4>Nora Whitfield</h4><div class="role">Co-Founder</div>Lorem ipsum dolor sit amet, consectetuer adipiscing elit, sed diam nonummy nibh euismod tincidunt.<div class="socials"><i></i><i></i><i></i></div></div></div>
  <div class="card" style="left:474px"><div class="photo" role="img" aria-label="Team member portrait"></div><div class="card-body"><h4>Maya Castell</h4><div class="role">Developer</div>Lorem ipsum dolor sit amet, consectetuer adipiscing elit, sed diam nonummy nibh euismod tincidunt.<div class="socials"><i></i><i></i><i></i></div></div></div>
  <div class="card" style="left:778px"><div class="photo" role="img" aria-label="Team member portrait"></div><div class="card-body"><h4>Lena Ortiz</h4><div class="role">Designer</div>Lorem ipsum dolor sit amet, consectetuer adipiscing elit, sed diam nonummy nibh euismod tincidunt.<div class="socials"><i></i><i></i><i></i></div></div></div>
  <div class="dots" style="top:663px"><i></i><i></i><i></i></div>
</section>

<section class="hiring" role="img" aria-label="Blue-tinted view up toward glass office towers">
  <h2>WE ARE HIRING</h2>
  <p>Lorem Ipsum is simply dummy text of the printing and typesetting industry. Lorem Ipsum has been the industry's standard dummy text ever since the 1500s, when an unknown printer took a galley of type and scrambled it to make a type specimen book.</p>
  <span class="btn-outline">APPLY</span>
</section>

<section class="expertise">
  <h3>EXPERTISE</h3>
  <div class="tag">PHASELLUS AUCTOR QUAM VITAE BIBENDUM TINCIDUNT</div>
  <div class="skill" style="left:170px;top:150px">Community Engagement <b>65%</b><div class="track"><div class="fill" style="width:65%"></div></div></div>
  <div class="skill" style="left:610px;top:150px">Deescalating Conflict <b>81%</b><div class="track"><div class="fill" style="width:81%"></div></div></div>
  <div class="skill" style="left:170px;top:198px">Navigating Policy <b>70%</b><div class="track"><div class="fill" style="width:70%"></div></div></div>
  <div class="skill" style="left:610px;top:198px">Energy Access – Reducing Energy Poverty <b>40%</b><div class="track"><div class="fill" style="width:40%"></div></div></div>
  <div class="skill" style="left:170px;top:246px">Investor Relations <b>29%</b><div class="track"><div class="fill" style="width:29%"></div></div></div>
</section>

<section class="posts">
  <h2 class="section-title" style="top:68px">LATEST POST</h2>
  <div class="section-sub" style="top:138px">Check our lasted news, stories, promotions and more...</div>
  <div class="card" style="left:170px"><div class="photo" role="img" aria-label="Professional working on a laptop"></div><div class="card-body"><h4 style="font-size:12px">THERE ARE A FEW THINGS</h4><p style="margin-top:12px">Lorem ipsum dolor sit amet, consectetuer adipiscing elit, sed diam nonummy nibh euismod tincidunt.</p><div class="read">Read More ⟶</div></div></div>
  <div class="card" style="left:474px"><div class="photo" role="img" aria-label="Professional at a desk"></div><div class="card-body"><h4 style="font-size:12px">CONTRARY TO POPULAR BELIEF</h4><p style="margin-top:12px">Lorem ipsum dolor sit amet, consectetuer adipiscing elit, sed diam nonummy nibh euismod tincidunt.</p><div class="read">Read More ⟶</div></div></div>
  <div class="card" style="left:778px"><div class="photo" role="img" aria-label="Professional in a workspace"></div><div class="card-body"><h4 style="font-size:12px">IT IS A LONG ESTABLISHED</h4><p style="margin-top:12px">Lorem ipsum dolor sit amet, consectetuer adipiscing elit, sed diam nonummy nibh euismod tincidunt.</p><div class="read">Read More ⟶</div></div></div>
  <div class="dots" style="top:636px"><i></i><i></i></div>
  <div class="btn-pill">VIEW MORE POSTS</div>
</section>

<section class="testimonial" role="img" aria-label="Blue-tinted office interior with people by tall windows">
  <h3>WHAT OUR CLIENT ARE SAYING</h3>
  <div class="section-sub">Don't just take our word</div>
  <div class="quote-box">Lorem Ipsum is simply dummy text of the printing and typesetting industry. Lorem Ipsum has been the industry's standard dummy text ever since the 1500s, when an unknown printer took a galley of type and scrambled it to make a type specimen book. It has survived not only five centuries, but also the leap into electronic typesetting, remaining essentially unchanged.</div>
  <svg class="quote-mark" viewBox="0 0 36 30"><path d="M2 28V16C2 8 6 3 13 2v5c-4 1-5 4-5 8h6v13zM21 28V16c0-8 4-13 11-14v5c-4 1-5 4-5 8h6v13z" fill="#fff"/></svg>
  <div class="avatar" role="img" aria-label="Client portrait"></div>
  <div class="client">Ada Brennan<small>Business Owner</small></div>
</section>

<footer class="site-footer">
  <svg class="notch" style="top:0" viewBox="0 0 80 30"><path d="M0 0 L40 26 L80 0Z" fill="#173e63"/><path d="M30 8 L40 15 L50 8" fill="none" stroke="#fff" stroke-width="2"/></svg>
  <div class="col" style="left:231px;width:280px">
    <h5>CONTACT US</h5>
    <p>Lorem ipsum dolor sit amet, consectetur adipiscing elit, sed do eiusmod tempor incididunt ut labore et dolore magna aliqua.</p>
    <div class="contact-line"><svg viewBox="0 0 12 12"><path d="M6 0a4 4 0 0 0-4 4c0 3 4 8 4 8s4-5 4-8a4 4 0 0 0-4-4z" fill="#85acd3"/></svg>Address Goes Here</div>
    <div class="contact-line"><svg viewBox="0 0 12 12"><path d="M2 1h3l1 3-2 1a7 7 0 0 0 3 3l1-2 3 1v3c-6 0-9-3-9-9z" fill="#85acd3"/></svg>(+01) 555 0142</div>
    <div class="contact-line"><svg viewBox="0 0 12 12"><rect x="0" y="2" width="12" height="8" fill="#85acd3"/><path d="M0 2l6 4 6-4" stroke="#0f1a26" fill="none"/></svg>hello@corvalisenergy.example</div>
  </div>
  <div class="col" style="left:578px"><h5>QUICK LINKS</h5><ul class="links"><li>HOME</li><li>ABOUT</li><li>TEAM</li><li>EXPERTISE</li><li>BLOG</li></ul></div>
  <div class="col" style="left:775px"><h5>SUBSCRIBE OUR NEWSLETTER</h5><div class="field">Name</div><div class="field">Email</div><span class="subscribe">SUBSCRIBE</span></div>
  <div class="foot-rule"></div>
  <div class="copy">© Copyright 2016. All Rights Reserved.</div>
  <div class="foot-brand"><span class="brand-mark"></span>Corvalis Energy</div>
  <div class="foot-social"><i></i><i></i><i></i><i></i></div>
</footer>

</body>
</html>
```